Newsletter Ad

I am looking for someone to design an advertisement for a mother's club newsletter. 4" wide X by 5" tall (and 2.5" wide X 5" tall if possible).

I'm a psychotherapist, so want the ad to look professional, but modern. I have a logo with my photo attached that can be incorporated into the design. The colors of my website are turquoise and white. I'd like to keep with that theme...so maybe some turquoise blocking to match the logo font color.

I'm uploading a logo as well as an ad draft with the content I'd like listed in the ad.

```html
<!DOCTYPE html>
<html lang="en">
<head>
<meta charset="utf-8">
<title>Dana Morel – Psychotherapy Ad</title>
<link rel="stylesheet" href="https://fonts.googleapis.com/css2?family=Didact+Gothic&display=swap">
<style>
  :root {
    --black: #0d0e0f;
    --teal-name: #3fb3ac;
    --teal-panel: #3b9a95;
    --teal-band: #1f7a75;
    --teal-mid: #2c8a85;
    --teal-deep: #1c5f5b;
    --gray-panel: #a3a5a6;
    --gray-text: #9c9c9c;
    --rule: #8a8a8a;
    --white: #ffffff;
    --ink: #111111;
  }
  * { box-sizing: border-box; margin: 0; padding: 0; }
  html, body { width: 961px; height: 1200px; overflow: hidden; background: var(--white); }
  body { font-family: "Didact Gothic", "Century Gothic", sans-serif; }
  .ad { position: relative; width: 961px; height: 1200px; overflow: hidden; background: var(--teal-panel); }

  .header { position: absolute; left: 0; top: 0; width: 961px; height: 377px; background: var(--black); }
  .portrait {
    position: absolute; left: 0; top: 0; width: 234px; height: 377px;
    background: linear-gradient(160deg, #6b7a52 0%, #a88a6a 40%, #d6b69a 60%, #2a2522 100%);
  }
  .name {
    position: absolute; left: 260px; width: 650px; top: 100px; text-align: center;
    color: var(--teal-name); font-size: 50px; font-weight: 400; line-height: 1; white-space: nowrap;
  }
  .name-rule { position: absolute; left: 311px; top: 178px; width: 555px; height: 2px; background: var(--rule); }
  .discipline {
    position: absolute; left: 260px; width: 650px; top: 205px; text-align: center;
    color: var(--gray-text); font-size: 62px; line-height: 1;
  }
  .clientele {
    position: absolute; left: 260px; width: 650px; top: 270px; text-align: center;
    color: var(--gray-text); font-size: 36px; line-height: 45px;
  }

  .divider-band { position: absolute; left: 0; top: 377px; width: 961px; height: 33px; background: var(--teal-band); }

  .side-panel {
    position: absolute; left: 0; top: 410px; width: 214px; height: 790px;
    background: linear-gradient(90deg, var(--teal-deep) 0%, var(--teal-mid) 50%, #1a3f3d 100%);
  }

  .specialties {
    position: absolute; left: 214px; top: 418px; width: 716px; list-style: none; text-align: center;
    color: var(--white); font-size: 40px; line-height: 60px;
  }

  .contact {
    position: absolute; left: 214px; top: 912px; width: 728px; height: 213px;
    background: var(--gray-panel); text-align: center; color: var(--ink);
    font-size: 37px; font-style: normal; line-height: 46.5px; padding-top: 20px;
  }
  .contact-band { position: absolute; left: 214px; top: 912px; width: 747px; height: 213px; background: var(--gray-panel); }
  .license {
    position: absolute; right: 34px; top: 1136px; color: var(--ink); font-size: 26px;
  }
</style>
</head>
<body>
<div class="ad">
  <header class="header">
    <div class="portrait" role="img" aria-label="Portrait photograph of the therapist"></div>
    <h1 class="name">DANA MOREL, MA, MFT</h1>
    <div class="name-rule"></div>
    <p class="discipline">Psychotherapy</p>
    <p class="clientele">for Individuals,<br>Couples and Families</p>
  </header>

  <div class="divider-band"></div>

  <div class="side-panel" role="img" aria-label="Decorative vertical stripe pattern in black and teal"></div>

  <ul class="specialties">
    <li>Parenting</li>
    <li>Depression</li>
    <li>Anxiety</li>
    <li>Life Transitions</li>
    <li>Divorce</li>
    <li>Couples Issues</li>
    <li>Women’s Issues</li>
    <li>Attachment and Neuroscience</li>
  </ul>

  <div class="contact-band"></div>
  <address class="contact">
    418 Alder Street, Fairbrook, CA 94018<br>
    www.danamorel.com<br>
    dana@danamorel.com<br>
    415.555.0148
  </address>

  <p class="license">License# MFC20481</p>
</div>
</body>
</html>
```